Book Cover Design

Design with title UNWAVERING
Subtitle: Ways to Kindle the Spark of Resolve
Author Name: Carla Jean Morrow
Put DAILY MERIDIAN BESTSELLER at top
Shimmer design, see inspirational images attached

```html
<!DOCTYPE html>
<html lang="en">
<head>
<meta charset="UTF-8">
<title>Unwavering — Book Cover</title>
<link rel="stylesheet" href="https://fonts.googleapis.com/css2?family=Barlow:wght@400;500;600&display=swap">
<style>
  :root {
    --page-bg: #dcdcdc;
    --mint: #a6e6cc;
    --cream: #f1efc9;
    --peach: #edcdc3;
    --lilac: #c7a8dc;
    --violet: #a36ddb;
    --periwinkle: #a8a9de;
    --ink: #1e1e22;
    --author-red: #c0262d;
    --subtitle-purple: #5d2a8f;
    --title-green: #68c98f;
    --title-lime: #b9e77f;
    --title-tan: #c9b07a;
    --title-gold: #e0c65a;
    --title-magenta: #c21ea6;
    --title-purple: #8a2fb8;
  }
  * { margin: 0; padding: 0; box-sizing: border-box; }
  html, body {
    width: 1200px;
    height: 900px;
    overflow: hidden;
    background: var(--page-bg);
  }
  .stage {
    position: relative;
    width: 1200px;
    height: 900px;
  }
  .book-cover {
    position: absolute;
    left: 302px;
    top: 30px;
    width: 596px;
    height: 840px;
    overflow: hidden;
    font-family: "Barlow", "Helvetica Neue", Arial, sans-serif;
    background:
      radial-gradient(ellipse 70% 55% at 0% 0%, var(--mint) 0%, rgba(166,230,204,0) 70%),
      radial-gradient(ellipse 60% 50% at 100% 5%, var(--peach) 0%, rgba(237,205,195,0) 75%),
      radial-gradient(ellipse 75% 55% at 5% 100%, var(--violet) 0%, rgba(163,109,219,0) 75%),
      radial-gradient(ellipse 60% 45% at 100% 100%, var(--periwinkle) 0%, rgba(168,169,222,0) 75%),
      linear-gradient(180deg, var(--cream) 0%, var(--cream) 45%, var(--lilac) 100%);
  }
  .bestseller-line {
    position: absolute;
    top: 30px;
    left: 0;
    width: 100%;
    text-align: center;
    padding-left: 20px;
    font-size: 15px;
    font-weight: 600;
    letter-spacing: 0.42em;
    color: var(--ink);
  }
  .author-name {
    position: absolute;
    top: 91px;
    left: 0;
    width: 100%;
    text-align: center;
    padding-left: 20px;
    font-size: 24px;
    font-weight: 500;
    letter-spacing: 0.03em;
    color: var(--author-red);
  }
  .title {
    position: absolute;
    left: 72px;
    top: 218px;
    font-size: 128px;
    font-weight: 500;
    line-height: 114px;
    letter-spacing: 0.01em;
  }
  .title-line {
    display: block;
    width: max-content;
    -webkit-background-clip: text;
    background-clip: text;
    color: transparent;
    filter: drop-shadow(3px 3px 0 rgba(220, 200, 170, 0.55));
  }
  .title-line--first {
    background-image: linear-gradient(90deg, var(--title-green) 0%, var(--title-lime) 50%, var(--title-tan) 100%);
    opacity: 0.85;
  }
  .title-line--second {
    background-image: linear-gradient(90deg, var(--title-tan) 0%, var(--title-lime) 45%, var(--title-gold) 100%);
    opacity: 0.8;
  }
  .title-line--third {
    background-image: linear-gradient(90deg, var(--title-purple) 0%, var(--title-magenta) 60%, #d23aa0 100%);
  }
  .subtitle {
    position: absolute;
    left: 78px;
    top: 590px;
    font-size: 25px;
    font-weight: 500;
    line-height: 33px;
    letter-spacing: 0.55em;
    color: var(--subtitle-purple);
  }
  .subtitle span { display: block; }
</style>
</head>
<body>
  <main class="stage">
    <article class="book-cover">
      <p class="bestseller-line">DAILY MERIDIAN BESTSELLER</p>
      <p class="author-name">CARLA JEAN MORROW</p>
      <h1 class="title" aria-label="Unwavering">
        <span class="title-line title-line--first">UNW</span>
        <span class="title-line title-line--second">AVE</span>
        <span class="title-line title-line--third">RING</span>
      </h1>
      <p class="subtitle" aria-label="Ways to Kindle the Spark of Resolve">
        <span>WAYS</span>
        <span>TO KINDLE</span>
        <span>THE</span>
        <span>SPARK</span>
        <span>OF</span>
        <span>RESOLVE</span>
      </p>
    </article>
  </main>
</body>
</html>
```